A gang member and street hustler turned preacher needs a cover

A man who used to be a gang member and street hustler turned his life around and became a preacher. He has written a book titled Unsteepled: My Passage From Ashes to Glory and he needs a cover for the book. The book is a memoir about his life and his journey from the streets to the church. It details the lessons that he's learned along the way. I have attached a photo to incorporate in the cover design. <br/>Title: Unsteepled: My Passage From Ashes to Glory<br/>Author: Dr. Marlon T. Grady

```html
<!DOCTYPE html>
<html lang="en">
<head>
<meta charset="utf-8">
<title>Unsteepled: My Passage From Ashes to Glory — Book Cover</title>
<link rel="stylesheet" href="https://fonts.googleapis.com/css2?family=Pinyon+Script&family=EB+Garamond:wght@400;500&display=swap">
<style>
  :root {
    --page-bg: #e6e6e8;
    --cover-deep: #0f0a1c;
    --cover-mid: #24163a;
    --cover-glow: #3a2552;
    --base-band: #0c0a1a;
    --gold: #e3c98e;
    --gold-soft: #cdb07a;
    --gold-light: #f6ead0;
    --portrait-dark: #1c1a2a;
    --portrait-mid: #3b3548;
  }
  * { margin: 0; padding: 0; box-sizing: border-box; }
  html, body {
    width: 939px;
    height: 1200px;
    overflow: hidden;
    background: var(--page-bg);
  }
  .book-cover {
    position: absolute;
    left: 177px;
    top: 176px;
    width: 567px;
    height: 849px;
    overflow: hidden;
    background:
      radial-gradient(ellipse 70% 55% at 55% 35%, var(--cover-glow) 0%, var(--cover-mid) 45%, var(--cover-deep) 100%);
  }
  .cover-title {
    position: absolute;
    left: 34px;
    top: 30px;
    width: 500px;
    font-family: "Pinyon Script", cursive;
    font-size: 104px;
    font-weight: 400;
    line-height: 1.1;
    color: var(--gold);
    letter-spacing: 1px;
    white-space: nowrap;
  }
  .cover-subtitle {
    position: absolute;
    left: 48px;
    top: 286px;
    font-family: "EB Garamond", serif;
    font-size: 38px;
    line-height: 57px;
    color: var(--gold-light);
    list-style: none;
  }
  .author-portrait {
    position: absolute;
    left: 165px;
    top: 190px;
    width: 402px;
    height: 560px;
    background:
      radial-gradient(ellipse 45% 30% at 48% 18%, var(--portrait-mid) 0%, transparent 70%),
      linear-gradient(180deg, rgba(28,26,42,0) 0%, var(--portrait-dark) 35%, var(--portrait-mid) 75%, var(--portrait-dark) 100%);
    border-radius: 160px 160px 0 0;
    opacity: 0.9;
  }
  .base-swoosh {
    position: absolute;
    left: 0;
    bottom: 0;
    width: 567px;
    height: 220px;
  }
  .cover-author {
    position: absolute;
    right: 36px;
    top: 770px;
    font-family: "EB Garamond", serif;
    font-size: 25px;
    color: var(--gold-light);
    letter-spacing: 0.5px;
  }
</style>
</head>
<body>
  <main class="book-cover">
    <h1 class="cover-title">Unsteepled</h1>

    <div class="author-portrait" role="img" aria-label="Portrait of the author seated in a dark suit with a white shirt and green pocket square"></div>

    <ul class="cover-subtitle">
      <li>My</li>
      <li>passage</li>
      <li>from</li>
      <li>ashes</li>
      <li>to</li>
      <li>glory</li>
    </ul>

    <svg class="base-swoosh" viewBox="0 0 567 220" aria-hidden="true">
      <defs>
        <linearGradient id="swoosh-gold" x1="0" y1="0" x2="1" y2="0">
          <stop offset="0" stop-color="#fff4dc"/>
          <stop offset="0.5" stop-color="#e3c98e"/>
          <stop offset="1" stop-color="#c9a868"/>
        </linearGradient>
      </defs>
      <path d="M0 190 C 160 120, 360 110, 567 70 L567 220 L0 220 Z" fill="var(--base-band)"/>
      <path d="M0 188 C 160 118, 360 106, 567 68 L567 76 C 360 114, 170 126, 0 196 Z" fill="url(#swoosh-gold)"/>
    </svg>

    <p class="cover-author">Dr Marlon T Grady</p>
  </main>
</body>
</html>
```